Lanternleaf - Fresh Asian Cuisine Menu

We need to redo our menu to include pictures of food items. Our restaurant is vibrant, trendy, upscale Chinese cuisine

Requirements
Must have
• Must fit on 8.5x11 paper. We can remove the About Us section if needed but menu cannot be more than 6 pages total. Must include pictures of menu items

```html
<!DOCTYPE html>
<html lang="en">
<head>
<meta charset="utf-8">
<title>Lanternleaf - Fresh Asian Cuisine Menu</title>
<link href="https://fonts.googleapis.com/css2?family=Montserrat:wght@600;700&family=Oswald:wght@300;400;500&display=swap" rel="stylesheet">
<style>
  :root {
    --gold: #f7ac16;
    --red: #d0232a;
    --red-dark: #a8151c;
    --ink: #1d1208;
    --photo-frame: #fff6e6;
  }
  * { box-sizing: border-box; margin: 0; padding: 0; }
  html, body { width: 927px; height: 1200px; overflow: hidden; }
  body { background: var(--gold); font-family: "Oswald", sans-serif; color: var(--ink); }
  .menu { position: relative; width: 927px; height: 1200px; background: var(--gold); }
  .frame { position: absolute; inset: 0; }

  .section-title {
    position: absolute; display: flex; align-items: center; gap: 12px;
    font-family: "Oswald", sans-serif; font-weight: 500; font-size: 28px;
    color: var(--red); text-transform: uppercase; letter-spacing: 0.2px; white-space: nowrap;
  }
  .section-title .band { height: 18px; background: var(--red); flex: 1; border-top: 3px solid var(--red-dark); border-bottom: 3px solid var(--red-dark); opacity: .9; }

  .divider { position: absolute; width: 3px; background: var(--red-dark); left: 462px; }

  .item { position: absolute; width: 381px; height: 92px; }
  .item.left { left: 68px; }
  .item.right { left: 483px; width: 376px; }

  .item .name {
    position: absolute; left: 0; top: 4px; width: 235px;
    font-family: "Montserrat", sans-serif; font-weight: 700; font-size: 17px; line-height: 1.15; color: var(--ink);
  }
  .item .name .spice { color: var(--red); font-size: 15px; margin-left: 10px; }
  .item .rule { position: absolute; left: 0; width: 34px; height: 2px; background: var(--red); }
  .item .price {
    position: absolute; right: 103px; top: 2px;
    font-family: "Montserrat", sans-serif; font-weight: 600; font-size: 20px; color: var(--ink);
  }
  .item .desc {
    position: absolute; left: 0; width: 245px;
    font-family: "Oswald", sans-serif; font-weight: 300; font-size: 10.5px; line-height: 1.45; color: var(--ink);
  }
  .item .photo {
    position: absolute; right: 0; top: 0; width: 88px; height: 88px;
    border: 3px solid var(--red-dark); border-radius: 7px; background: var(--photo-frame); padding: 4px;
  }
  .item .photo span { display: block; width: 100%; height: 100%; border-radius: 3px; }

  .item.right .name, .item.right .rule, .item.right .desc { left: 103px; }
  .item.right .price { right: 0; }
  .item.right .photo { left: 0; right: auto; }
  .item.indent .name, .item.indent .desc { left: 31px; }

  .warm { background: linear-gradient(135deg, #c98a3a, #7a3b12); }
  .pale { background: linear-gradient(135deg, #efe3c4, #b9a06a); }
  .green { background: linear-gradient(135deg, #5e7a2c, #1f2e12); }
  .red { background: linear-gradient(135deg, #c2451e, #6a1a0c); }
  .purple { background: linear-gradient(135deg, #6d4a6a, #2a1a24); }
  .mixed { background: linear-gradient(135deg, #d8b457, #6a8a3a); }
  .choc { background: linear-gradient(135deg, #6a2a20, #2a0e0a); }
  .crisp { background: linear-gradient(135deg, #e0b070, #8a4a2a); }
</style>
</head>
<body>
<main class="menu">
  <svg class="frame" width="927" height="1200" viewBox="0 0 927 1200" aria-hidden="true">
    <rect x="34" y="34" width="859" height="1132" fill="none" stroke="#d0232a" stroke-width="5"/>
    <rect x="46" y="46" width="835" height="1108" fill="none" stroke="#d0232a" stroke-width="2"/>
    <g fill="none" stroke="#d0232a" stroke-width="4">
      <path d="M52 110 V52 H110"/><path d="M62 96 V62 H96"/>
      <path d="M875 110 V52 H817"/><path d="M865 96 V62 H831"/>
      <path d="M52 1090 V1148 H110"/><path d="M62 1104 V1138 H96"/>
      <path d="M875 1090 V1148 H817"/><path d="M865 1104 V1138 H831"/>
    </g>
  </svg>

  <h2 class="section-title" style="left:166px; top:48px; width:595px;"><span class="band"></span>Noodles &amp; Rice<span class="band"></span></h2>
  <h2 class="section-title" style="left:68px; top:312px; width:791px;"><span class="band"></span>Vegetarian Dishes<span class="band"></span></h2>
  <h2 class="section-title" style="left:68px; top:681px; width:383px;"><span class="band"></span>Kids Menu<span class="band"></span></h2>
  <h2 class="section-title" style="left:476px; top:681px; width:383px;"><span class="band"></span>Desserts<span class="band"></span></h2>

  <div class="divider" style="top:110px; height:190px;"></div>
  <div class="divider" style="top:347px; height:320px;"></div>
  <div class="divider" style="top:727px; height:410px;"></div>

  <!-- Noodles & Rice -->
  <article class="item left" style="top:106px;">
    <h3 class="name">Lanternleaf's Fried Rice</h3><span class="price">$12</span>
    <span class="rule" style="top:28px"></span>
    <p class="desc" style="top:34px">Shrimp, chicken, and beef, farm fresh eggs, onions, and scallions</p>
    <div class="photo"><span class="pale" role="img" aria-label="Photo of fried rice"></span></div>
  </article>
  <article class="item right" style="top:106px;">
    <h3 class="name">Lanternleaf's Lo Mein</h3><span class="price">$12</span>
    <span class="rule" style="top:28px"></span>
    <p class="desc" style="top:34px">Shrimp, chicken, and beef, farm fresh eggs, onions, and scallions</p>
    <div class="photo"><span class="warm" role="img" aria-label="Photo of lo mein"></span></div>
  </article>
  <article class="item left" style="top:214px;">
    <h3 class="name">Vegetarian White<br>Fried Rice</h3><span class="price">$10</span>
    <span class="rule" style="top:46px"></span>
    <p class="desc" style="top:52px">Mixed vegetables with white rice</p>
    <div class="photo"><span class="mixed" role="img" aria-label="Photo of vegetable fried rice"></span></div>
  </article>
  <article class="item right" style="top:214px;">
    <h3 class="name">Vegetarian Lo Mein<span class="spice">🌶</span></h3><span class="price">$10</span>
    <span class="rule" style="top:28px"></span>
    <p class="desc" style="top:34px">Mixed vegetables with lo mein noodles</p>
    <div class="photo"><span class="warm" role="img" aria-label="Photo of vegetable lo mein"></span></div>
  </article>

  <!-- Vegetarian -->
  <article class="item left" style="top:364px;">
    <h3 class="name">Wok Tossed String Beans</h3><span class="price">$9</span>
    <span class="rule" style="top:28px"></span>
    <p class="desc" style="top:34px">Fresh string beans mixed with pickled vegetables</p>
    <div class="photo"><span class="green" role="img" aria-label="Photo of string beans"></span></div>
  </article>
  <article class="item right" style="top:364px;">
    <h3 class="name">Buddha's Delight</h3><span class="price">$10</span>
    <span class="rule" style="top:28px"></span>
    <p class="desc" style="top:34px">Seasonal vegetables wok-tossed in our light soy garlic sauce</p>
    <div class="photo"><span class="mixed" role="img" aria-label="Photo of mixed vegetables"></span></div>
  </article>
  <article class="item left" style="top:471px;">
    <h3 class="name">Mapo Tofu<span class="spice">🌶🌶</span></h3><span class="price">$11</span>
    <span class="rule" style="top:28px"></span>
    <p class="desc" style="top:34px">Soft Tofu, scallion, Sichuan peppercorn and peppers</p>
    <div class="photo"><span class="red" role="img" aria-label="Photo of mapo tofu"></span></div>
  </article>
  <article class="item right" style="top:471px;">
    <h3 class="name">Stir-fried Eggplant<span class="spice">🌶</span><br>Beans</h3><span class="price">$12</span>
    <span class="rule" style="top:46px"></span>
    <p class="desc" style="top:52px">Chinese eggplant with sautéed green beans</p>
    <div class="photo"><span class="purple" role="img" aria-label="Photo of eggplant and beans"></span></div>
  </article>
  <article class="item left" style="top:578px;">
    <h3 class="name">Spicy Garlic Eggplant<span class="spice">🌶</span></h3><span class="price">$12</span>
    <span class="rule" style="top:28px"></span>
    <p class="desc" style="top:34px">Chinese eggplant in spicy garlic sauce garnished with scallions</p>
    <div class="photo"><span class="purple" role="img" aria-label="Photo of garlic eggplant"></span></div>
  </article>
  <article class="item right" style="top:578px;">
    <h3 class="name">Shiitake Baby<br>Bok-Choy</h3><span class="price">$12</span>
    <span class="rule" style="top:46px"></span>
    <p class="desc" style="top:52px">Sautéed baby bok-choy with Shiitake mushrooms in brown sauce</p>
    <div class="photo"><span class="green" role="img" aria-label="Photo of bok-choy with mushrooms"></span></div>
  </article>

  <!-- Kids -->
  <article class="item left" style="top:730px;">
    <h3 class="name">Beef Lo Mein</h3><span class="price">$5</span>
    <span class="rule" style="top:28px"></span>
    <p class="desc" style="top:34px">Lo Mein noodles mixed with beef in garlic sauce</p>
    <div class="photo"><span class="warm" role="img" aria-label="Photo of beef lo mein"></span></div>
  </article>
  <article class="item left" style="top:836px;">
    <h3 class="name">Chicken Fried Rice</h3><span class="price">$5</span>
    <span class="rule" style="top:28px"></span>
    <p class="desc" style="top:34px">Fried rice, farm fresh eggs, onions, and scallions</p>
    <div class="photo"><span class="pale" role="img" aria-label="Photo of chicken fried rice"></span></div>
  </article>
  <article class="item left" style="top:944px;">
    <h3 class="name">Sweet &amp; Sour Chicken</h3><span class="price">$6</span>
    <span class="rule" style="top:28px"></span>
    <p class="desc" style="top:34px">Bite sized crispy chicken with sweet &amp; sour sauce</p>
    <div class="photo"><span class="red" role="img" aria-label="Photo of sweet and sour chicken"></span></div>
  </article>
  <article class="item left indent" style="top:1050px;">
    <h3 class="name">Lemon Chicken</h3><span class="price">$6</span>
    <p class="desc" style="top:28px">Bite sized crispy chicken in a sweet lemon sauce</p>
    <div class="photo"><span class="pale" role="img" aria-label="Photo of lemon chicken"></span></div>
  </article>

  <!-- Desserts -->
  <article class="item right" style="top:730px;">
    <h3 class="name">The Great Wall of Cake</h3><span class="price">$7</span>
    <span class="rule" style="top:28px"></span>
    <p class="desc" style="top:34px">Scale this fortress of Chocolate Cake Delight</p>
    <div class="photo"><span class="choc" role="img" aria-label="Photo of chocolate layer cake"></span></div>
  </article>
  <article class="item right" style="top:836px;">
    <h3 class="name">Cheesecake Wontons (4)</h3><span class="price">$6</span>
    <span class="rule" style="top:28px"></span>
    <p class="desc" style="top:34px">Fried wontons stuffed with cheesecake and dipped in raspberry sauce</p>
    <div class="photo"><span class="crisp" role="img" aria-label="Photo of cheesecake wontons"></span></div>
  </article>
  <article class="item right" style="top:944px;">
    <h3 class="name">Tempura Snowball</h3><span class="price">$4</span>
    <span class="rule" style="top:28px"></span>
    <p class="desc" style="top:34px">Vanilla ice cream fried in tempura batter with powdered sugar and fudge</p>
    <div class="photo"><span class="crisp" role="img" aria-label="Photo of tempura fried ice cream"></span></div>
  </article>
  <article class="item right" style="top:1050px;">
    <h3 class="name">Sweet Rice Patties in<br>Caramel</h3><span class="price">$7</span>
    <span class="rule" style="top:46px"></span>
    <p class="desc" style="top:52px">Traditional Chinese dessert with sweet rice dipped in a caramel sauce</p>
    <div class="photo"><span class="choc" role="img" aria-label="Photo of caramel rice patties"></span></div>
  </article>
</main>
</body>
</html>
```